Stonelynk Business Card Design

The Stonelynk Co is an aggregate (crushing) equipment dealer serving Western Canadian provinces. Stonelynk is a distributor of aggregate equipment for different manufacturers.

We are looking to change and update the existing business card which has been used since the existence of the company. A copy of existing card has been attached for reference. The Stonelynk Co logo we want to remain the same and we want the green color to remain the same.

We are wanting something new with a different look. A refreshing card to show a new modern and updated look. No longer wanting to have the manufacturers on the back of the card but something more like our logo on the back of the card with a statement like "Crushing Solutions"

ideas could be:
- card can be different colors on front and back
- front or reverse of the card could possibly be the green color with the logo in black

Target Market(s)

Owners of Aggregate/Crushing companies

Requirements
Must have
• - logo to remain same along with same font within logo
• - green color to remain same
Nice to have
• as noted above under project description
Should not have

```html
<!DOCTYPE html>
<html lang="en">
<head>
<meta charset="utf-8">
<title>The Stonelynk Co – Business Card</title>
<link href="https://fonts.googleapis.com/css2?family=Archivo:wght@700&family=Roboto+Mono:wght@500&family=Saira+Stencil+One&display=swap" rel="stylesheet">
<style>
  :root {
    --brand-green: #7f8133;
    --ink: #0d0d0d;
    --paper: #ffffff;
    --stage: #d8d3ca;
    --steel-dark: #141414;
    --steel-mid: #262626;
    --chrome-light: #e9e9e9;
    --chrome-dark: #6a6a6a;
  }
  * { margin: 0; padding: 0; box-sizing: border-box; }
  html, body { width: 900px; height: 1200px; overflow: hidden; }
  body { background: var(--stage); position: relative; }

  .card {
    position: absolute; left: 88px; width: 732px; height: 428px;
    border-radius: 22px; overflow: hidden;
    box-shadow: 0 6px 14px rgba(0,0,0,.35);
  }

  /* Front */
  .card-front { top: 137px; background: var(--paper); }
  .name-tab { position: absolute; left: 0; top: 0; }
  .holder-name {
    position: absolute; left: 47px; top: 20px;
    font: 32px "Saira Stencil One", sans-serif; color: var(--paper); letter-spacing: 1px;
  }
  .direct-line {
    position: absolute; left: 48px; top: 58px;
    font: 19px "Saira Stencil One", sans-serif; color: var(--brand-green); letter-spacing: 1px;
  }
  .brand-mark {
    position: absolute; left: 45px; top: 160px; width: 330px; text-align: center;
  }
  .brand-dot {
    display: block; width: 72px; height: 72px; margin: 0 auto 22px;
    border-radius: 50%; background: var(--brand-green);
  }
  .brand-name {
    font: 700 27px "Archivo", sans-serif; color: var(--ink); letter-spacing: .3px; white-space: nowrap;
  }

  .contact-list { position: absolute; left: 420px; top: 101px; list-style: none; }
  .contact-row { display: flex; gap: 7px; margin-bottom: 11px; height: 29px; }
  .contact-row.address { height: 64px; }
  .contact-icon {
    width: 31px; border-radius: 5px; background: var(--brand-green);
    display: flex; align-items: center; justify-content: center;
  }
  .contact-text {
    width: 231px; border-radius: 5px; background: var(--ink); color: var(--paper);
    font: 500 15px "Roboto Mono", monospace; letter-spacing: .8px;
    display: flex; flex-direction: column; justify-content: center; padding-left: 7px; line-height: 20px;
  }

  .product-band {
    position: absolute; left: 0; bottom: 0; width: 100%; height: 60px;
    background: var(--brand-green); color: var(--paper);
    font: 26px "Saira Stencil One", sans-serif; letter-spacing: .5px;
    display: flex; align-items: center; justify-content: center; padding-top: 2px;
  }

  /* Back */
  .card-back { top: 633px; }
  .mesh-surface {
    position: absolute; inset: 0;
    background: radial-gradient(ellipse at 50% 45%, var(--steel-mid), var(--steel-dark) 75%);
  }
  .chrome-rule {
    position: absolute; left: 0; width: 100%; height: 7px;
    background: linear-gradient(180deg, var(--chrome-dark), var(--chrome-light) 45%, var(--chrome-dark));
  }
  .chrome-rule.top { top: 68px; }
  .chrome-rule.bottom { top: 350px; }
  .back-mark { position: absolute; left: 0; top: 120px; width: 100%; text-align: center; }
  .back-mark .brand-dot { width: 84px; height: 84px; margin-bottom: 34px; }
  .back-name { font: 700 37px "Archivo", sans-serif; color: var(--paper); letter-spacing: .5px; }
  .tagline {
    margin-top: 4px; font: 700 21px "Archivo", sans-serif;
    color: var(--brand-green); letter-spacing: 4.5px;
  }
</style>
</head>
<body>

<section class="card card-front" aria-label="Business card front">
  <svg class="name-tab" width="415" height="101" viewBox="0 0 415 101" aria-hidden="true">
    <path d="M0 0 H412 L330 88 Q318 101 300 101 H0 Z" fill="var(--ink)"/>
  </svg>
  <h1 class="holder-name">DEREK HALVORSEN</h1>
  <p class="direct-line">DIRECT: 780.555.0142</p>

  <div class="brand-mark">
    <span class="brand-dot"></span>
    <p class="brand-name">THE STONELYNK CO.</p>
  </div>

  <ul class="contact-list">
    <li class="contact-row">
      <span class="contact-icon"><svg width="18" height="18" viewBox="0 0 24 24"><path d="M6.6 10.8a15 15 0 0 0 6.6 6.6l2.2-2.2a1 1 0 0 1 1-.25 11.4 11.4 0 0 0 3.6.57 1 1 0 0 1 1 1V20a1 1 0 0 1-1 1A17 17 0 0 1 3 4a1 1 0 0 1 1-1h3.5a1 1 0 0 1 1 1c0 1.25.2 2.45.57 3.57a1 1 0 0 1-.25 1z" fill="#fff"/></svg></span>
      <span class="contact-text">780.555.0177</span>
    </li>
    <li class="contact-row">
      <span class="contact-icon"><svg width="18" height="18" viewBox="0 0 24 24"><path d="M6 3h12v5H6zM4 9h16a2 2 0 0 1 2 2v6h-4v4H6v-4H2v-6a2 2 0 0 1 2-2zm4 7v3h8v-3z" fill="#fff"/></svg></span>
      <span class="contact-text">780.555.0158</span>
    </li>
    <li class="contact-row">
      <span class="contact-icon"><svg width="19" height="15" viewBox="0 0 24 18"><rect x="1" y="1" width="22" height="16" rx="1" fill="none" stroke="#fff" stroke-width="2"/><path d="M1 2l11 8 11-8" fill="none" stroke="#fff" stroke-width="2"/></svg></span>
      <span class="contact-text">DEREK@STONELYNK.COM</span>
    </li>
    <li class="contact-row">
      <span class="contact-icon"><svg width="19" height="19" viewBox="0 0 24 24" fill="none" stroke="#fff" stroke-width="1.8"><circle cx="12" cy="12" r="10"/><ellipse cx="12" cy="12" rx="4.5" ry="10"/><path d="M2 12h20M4 6.5h16M4 17.5h16"/></svg></span>
      <span class="contact-text">WWW.STONELYNK.CA</span>
    </li>
    <li class="contact-row address">
      <span class="contact-icon"><svg width="16" height="22" viewBox="0 0 16 22"><path d="M8 0a8 8 0 0 1 8 8c0 6-8 14-8 14S0 14 0 8a8 8 0 0 1 8-8zm0 5a3 3 0 1 0 0 6 3 3 0 0 0 0-6z" fill="#fff"/></svg></span>
      <span class="contact-text"><span>5312-71B AVENUE</span><span>NISKU, ALBERTA T9E 2K8</span></span>
    </li>
  </ul>

  <p class="product-band">SCREENERS&nbsp;•&nbsp;CRUSHERS&nbsp;•&nbsp;CONVEYORS&nbsp;•&nbsp;SHREDDERS</p>
</section>

<section class="card card-back" aria-label="Business card back">
  <div class="mesh-surface" role="img" aria-label="Dark perforated metal mesh texture"></div>
  <div class="chrome-rule top"></div>
  <div class="chrome-rule bottom"></div>
  <div class="back-mark">
    <span class="brand-dot"></span>
    <p class="back-name">THE STONELYNK CO.</p>
    <p class="tagline">CRUSHING SOLUTIONS</p>
  </div>
</section>

</body>
</html>
```